Industrial Services company needs a business card design

We provide industrial maintenance services including sandblasting, painting, pressure washing, storage tank rehabilitation, and welding. I would like an industrial design that's eye catching. I would like the back-side of the card to list our services.

Industry/Entity Type

Construction

Contact Information for Business Card

address: 418 Bramblewood Lane, York, PA 17408
Phone: 410-637-1584
email: quellaninc@mailbrook.net
Walter Brennigan, President
www.quellanpainting.net

Logo Text

Quellan Industrial Services

Font styles to use
Sans Serif

Colors
000000
229ed3
0692cd
ffffff

Requirements
Must have
• Easy to read
• our services listed/included on back of card
• eye catching color combinations
Nice to have
• Water storage tank image

```html
<!DOCTYPE html>
<html lang="en">
<head>
<meta charset="utf-8">
<title>Quellan Industrial Services – Business Card</title>
<link rel="stylesheet" href="https://fonts.googleapis.com/css2?family=Questrial&display=swap">
<style>
  :root {
    --ink: #000000;
    --card-black: #06080a;
    --brand-blue: #0692cd;
    --band-blue: #1a93d0;
    --paper: #ffffff;
  }
  * { box-sizing: border-box; margin: 0; padding: 0; }
  html, body {
    width: 914px;
    height: 1200px;
    overflow: hidden;
    background: var(--paper);
    font-family: "Questrial", "Century Gothic", sans-serif;
  }
  .sheet { position: relative; width: 914px; height: 1200px; }

  .band-blue { position: absolute; left: 0; top: 0; width: 914px; height: 41px; background: var(--band-blue); }
  .band-black { position: absolute; left: 0; top: 41px; width: 914px; height: 17px; background: var(--ink); }

  /* Brand name block standing where the mark sits */
  .brand-mark {
    position: absolute; display: flex; align-items: center;
  }
  .brand-mark .dot { flex: none; border-radius: 50%; }
  .brand-mark .name { line-height: 1.12; }

  .brand-mark.hero {
    left: 340px; top: 122px; width: 240px; height: 160px;
    gap: 18px; color: var(--ink); font-size: 34px;
  }
  .brand-mark.hero .dot { width: 40px; height: 40px; background: var(--ink); }

  .brand-url {
    position: absolute; left: 0; top: 295px; width: 914px; text-align: center;
    color: var(--brand-blue); font-size: 21px; font-weight: 700; letter-spacing: 0.3px;
  }

  .palette { position: absolute; top: 354px; left: 375px; display: flex; gap: 30px; }
  .swatch { width: 32px; text-align: center; font-size: 8px; color: var(--ink); }
  .swatch .chip { width: 32px; height: 32px; margin-bottom: 3px; }
  .chip.black { background: var(--ink); }
  .chip.blue { background: var(--brand-blue); }
  .chip.white { background: var(--paper); border: 1.5px solid var(--ink); }

  .card { position: absolute; top: 441px; width: 397px; height: 247px; }
  .card-back { left: 41px; background: var(--card-black); }
  .card-front { left: 464px; background: var(--paper); border: 2px solid var(--ink); }

  .card-back .brand-mark {
    left: 143px; top: 66px; width: 120px; height: 90px;
    gap: 9px; color: var(--brand-blue); font-size: 16px;
  }
  .card-back .brand-mark .dot { width: 18px; height: 18px; background: var(--brand-blue); }
  .card-back .card-url {
    position: absolute; left: 0; top: 185px; width: 100%; text-align: center;
    color: var(--brand-blue); font-size: 8px;
  }
  .card-back .services {
    position: absolute; left: 0; top: 204px; width: 100%; text-align: center;
    color: var(--paper); font-size: 7px; letter-spacing: 0.4px; list-style: none;
  }
  .card-back .services li { display: inline; }
  .card-back .services li + li::before { content: "·"; color: var(--brand-blue); margin: 0 5px; }

  .card-front .brand-mark {
    left: 40px; top: 70px; width: 120px; height: 92px;
    gap: 9px; color: var(--brand-blue); font-size: 15px;
  }
  .card-front .brand-mark .dot { width: 18px; height: 18px; background: var(--brand-blue); }
  .card-front .holder {
    position: absolute; left: 182px; top: 86px; color: var(--brand-blue);
  }
  .holder .person { font-size: 15px; font-weight: 700; text-transform: uppercase; letter-spacing: 0.1px; }
  .holder .role { font-size: 15px; font-weight: 700; margin-top: 3px; }
  .holder .details { margin-top: 8px; font-size: 8px; line-height: 1.25; border-collapse: collapse; }
  .holder .details td { padding: 0; }
  .holder .details .label { padding-right: 2px; }
</style>
</head>
<body>
<div class="sheet">
  <div class="band-blue"></div>
  <div class="band-black"></div>

  <div class="brand-mark hero">
    <span class="dot"></span>
    <span class="name">Quellan<br>Industrial<br>Services</span>
  </div>
  <div class="brand-url">www.quellanpainting.net</div>

  <div class="palette">
    <div class="swatch"><div class="chip black"></div>#000000</div>
    <div class="swatch"><div class="chip blue"></div>#0692cd</div>
    <div class="swatch"><div class="chip white"></div>#ffffff</div>
  </div>

  <section class="card card-back">
    <div class="brand-mark">
      <span class="dot"></span>
      <span class="name">Quellan<br>Industrial<br>Services</span>
    </div>
    <div class="card-url">www.quellanpainting.net</div>
    <ul class="services">
      <li>Sandblasting</li><li>Painting</li><li>Pressure Washing</li><li>Tank Rehabilitation</li><li>Welding</li>
    </ul>
  </section>

  <section class="card card-front">
    <div class="brand-mark">
      <span class="dot"></span>
      <span class="name">Quellan<br>Industrial<br>Services</span>
    </div>
    <div class="holder">
      <div class="person">Walter Brennigan</div>
      <div class="role">President</div>
      <table class="details">
        <tr><td class="label">address</td><td>: 418 Bramblewood Lane, York, PA 17408</td></tr>
        <tr><td class="label">Phone</td><td>: 410-637-1584</td></tr>
        <tr><td class="label">email</td><td>: quellaninc@mailbrook.net</td></tr>
      </table>
    </div>
  </section>
</div>
</body>
</html>
```